Graphic Design Project

We need a single page design that will be used as a regular white paper, providing communication advice & techniques.

We have an example that needs upgrading to look more professional and exciting.

Logo and icons will be provided.

Image provided for this example but will need to be able to add and remove new images relative to each new white paper.

Design will need to be on a format that is easily editable and can be converted into a PDF document. e.g MS Word.

Target Market(s)

Existing and potential corporate individuals and organisations

Industry/Entity Type

Communication

Requirements
Must have
• Logo, Icons & web address

```html
<!DOCTYPE html>
<html lang="en">
<head>
<meta charset="utf-8">
<title>The Seven Deadly Sins of Presenting with Slides</title>
<link rel="stylesheet" href="https://fonts.googleapis.com/css2?family=Lato:wght@400;700;900&display=swap">
<style>
  :root {
    --backdrop: #dedede;
    --paper: #ffffff;
    --ink: #3d3d3d;
    --ink-soft: #555555;
    --banner: #6b6c6e;
    --green: #8cb31f;
    --brown: #7a6651;
    --orange: #f39a2b;
    --photo-light: #e4e4e4;
    --photo-dark: #8e8e8e;
  }
  * { box-sizing: border-box; margin: 0; padding: 0; }
  html, body {
    width: 1200px; height: 900px; overflow: hidden;
    background: var(--backdrop);
    font-family: "Lato", Arial, sans-serif;
    color: var(--ink);
  }
  .sheet {
    position: absolute; left: 290px; top: 14px;
    width: 620px; height: 872px;
    background: var(--paper);
    box-shadow: 0 2px 10px rgba(0,0,0,0.12);
  }
  .brand {
    position: absolute; left: 190px; top: 40px;
    display: flex; align-items: center; gap: 10px;
  }
  .brand-dot { width: 22px; height: 22px; border-radius: 50%; background: var(--green); }
  .brand-name {
    font-size: 30px; font-weight: 900; letter-spacing: -0.5px;
    color: var(--ink); line-height: 1;
  }
  .topic-icons {
    position: absolute; right: 34px; top: 96px;
    display: flex; gap: 14px;
  }
  .topic-icon {
    width: 34px; height: 34px; border-radius: 50%;
    display: flex; align-items: center; justify-content: center;
  }
  .topic-icon span { width: 18px; height: 18px; border-radius: 50%; border: 2px solid #fff; }
  .topic-icon.green { background: var(--green); }
  .topic-icon.brown { background: var(--brown); }
  .topic-icon.orange { background: var(--orange); }
  .title-band { position: absolute; left: 28px; top: 140px; width: 572px; height: 40px; }
  .title-text {
    position: absolute; left: 64px; top: 148px;
    font-size: 19px; font-weight: 900; color: #fff; letter-spacing: 0.2px;
  }
  .column { position: absolute; top: 200px; width: 252px; }
  .column.left { left: 40px; }
  .column.right { left: 326px; top: 262px; }
  .intro, .sin p {
    font-size: 10px; line-height: 1.38; color: var(--ink-soft);
    text-align: justify;
  }
  .intro { margin-bottom: 12px; }
  .feature-image {
    width: 252px; height: 112px; border-radius: 10px;
    background: linear-gradient(180deg, var(--photo-light), var(--photo-dark));
    margin-bottom: 14px;
  }
  .sin { margin-bottom: 9px; }
  .sin h2 {
    font-size: 10.5px; font-weight: 700; color: var(--green);
    display: flex; align-items: center; gap: 6px; margin-bottom: 2px;
  }
  .sin h2::before {
    content: ""; width: 0; height: 0;
    border-left: 6px solid var(--green);
    border-top: 4px solid transparent; border-bottom: 4px solid transparent;
  }
  .footer-rule {
    position: absolute; left: 40px; right: 40px; top: 690px;
    height: 1px; background: var(--green);
  }
  .footer {
    position: absolute; left: 40px; top: 702px;
    font-size: 10.5px; color: var(--ink-soft);
    display: flex; align-items: center; gap: 8px;
  }
  .footer::before {
    content: ""; width: 0; height: 0;
    border-left: 6px solid var(--green);
    border-top: 4px solid transparent; border-bottom: 4px solid transparent;
  }
  .footer a { color: var(--green); font-weight: 700; text-decoration: none; }
</style>
</head>
<body>
<article class="sheet">
  <header>
    <div class="brand">
      <span class="brand-dot"></span>
      <span class="brand-name">Brightline Communications</span>
    </div>
    <div class="topic-icons">
      <div class="topic-icon green"><span></span></div>
      <div class="topic-icon brown"><span></span></div>
      <div class="topic-icon orange"><span></span></div>
    </div>
    <svg class="title-band" viewBox="0 0 572 40" aria-hidden="true">
      <polygon points="0,0 552,0 572,40 0,40" fill="var(--banner)"/>
      <polygon points="14,15 24,20 14,25" fill="var(--green)"/>
    </svg>
    <h1 class="title-text">The Seven Deadly Sins of Presenting with Slides</h1>
  </header>

  <section class="column left">
    <p class="intro">There is an increasing expectation for organisational professionals to communicate using slide-ware technology such as SlideMaker, StageDeck and Zoomly, all great tools for enhancing our message. Yet we have all sat through presentations where technology takes over, working against the presenter where amongst the fumbling and mumbling the message is lost. Enhance your message, improve credibility and connect with your audience by avoiding these seven deadly sins of presenting with slides:</p>
    <div class="feature-image" role="img" aria-label="Silhouette figures in a row beside a presenter at a lectern"></div>
    <div class="sin">
      <h2>1. Rely on technology</h2>
      <p>Batteries go flat, software crashes, lights go out and speakers breakdown, we all know it and yet we rarely give ourselves enough time to set up, test and re-test our presentation tools.</p>
    </div>
    <div class="sin">
      <h2>2. Read your slides</h2>
      <p>Slides are fantastic, we love them for their ability to enhance the spoken word but they are not the message itself. Reading your slides will kill your credibility and engagement, please don't do it!</p>
    </div>
  </section>

  <section class="column right">
    <div class="sin">
      <h2>3. Dim the lights</h2>
      <p>Low light sends us a subconscious signal to relax and prepare for sleep, probably not the emotional state you want your audience in! Wherever possible set your room with natural light that doesn't glare the screen.</p>
    </div>
    <div class="sin">
      <h2>4. Appoint a 'Slider'</h2>
      <p>A Slider is a person who is asked to press the 'Enter' key to move the slides on your behalf. Lovely people but a complete distraction and incapable of working in sync with your natural rhythm. Insist on a wireless slider clicker, discreet and highly effective.</p>
    </div>
    <div class="sin">
      <h2>5. Deliver a monologue</h2>
      <p>Effective communication is a two way street. Where possible move away from your slides, even blank the screen to engage with your audience.</p>
    </div>
    <div class="sin">
      <h2>6. Get stuck in the mud</h2>
      <p>Being conscious of the projector light is a good thing but don't get physically stuck in one position while trying to avoid a shadow on the screen.</p>
    </div>
    <div class="sin">
      <h2>7. Using your slides as a prompt</h2>
      <p>If you don't know what slide is next you will fall into the 'click, pause, deliver' trap where you are reliant on your slides for what to say next. Know your stuff and create verbal segways between slides to deliver consistency and flow.</p>
    </div>
  </section>

  <div class="footer-rule"></div>
  <footer class="footer">For more information visit <a href="#">www.brightlinecommunications.com.au</a></footer>
</article>
</body>
</html>
```